tourism marketplace web app redesign*

Hi, I need our front-page redesigned. For the competition please submit a jpg of ABOVE THE FOLD ONLY. The full page redesign will be a revision request. URL is https://qp.trolvexa.hu/hu/index.html login:'fullhd' and password:'asdasd' (Fold is supposed to be at "Kiemelt Ajanlatok", use all elements above that. Please use at least one extra color other than the two in the logo, or you may completely change them. FOCUS should be on the central combined search box (3 dropdown, 2 calendar picker + Kereses Button) just like nestorly.com, ravimoto.com, Pelusi.com, etc... The search box is always large, central, white, we want that too. We want it to look more modern, more clean AND we want to feature a changing beautiful nature photo background (like nestorly.com).Please use our newly designed logo (in attached pdf) and use that new spelling: "ferntrail.online"

```html
<!DOCTYPE html>
<html lang="hu">
<head>
<meta charset="utf-8">
<title>ferntrail.online – Foglalj közvetlen a vadászterületnél</title>
<link href="https://fonts.googleapis.com/css2?family=Ubuntu:wght@400;500;700&family=Open+Sans:wght@300;400&display=swap" rel="stylesheet">
<style>
  :root {
    --teal: #65ae97;
    --teal-dark: #5a9f89;
    --nav-bg: #3f3f41;
    --ink: #333335;
    --muted: #8a8a8a;
    --field-border: #d6d6d6;
    --white: #ffffff;
  }
  * { box-sizing: border-box; margin: 0; padding: 0; }
  html, body { width: 1200px; height: 541px; overflow: hidden; background: var(--white); }
  body { position: relative; font-family: "Ubuntu", sans-serif; color: var(--ink); }

  .utility-bar { position: absolute; top: 0; left: 0; width: 1200px; height: 26px; background: var(--white); font-size: 9.5px; }
  .utility-bar .lang { position: absolute; left: 160px; top: 7px; font-family: "Open Sans", sans-serif; }
  .utility-bar .currency { position: absolute; left: 828px; top: 7px; font-family: "Open Sans", sans-serif; }
  .caret { display: inline-block; width: 0; height: 0; border-left: 3.5px solid transparent; border-right: 3.5px solid transparent; border-top: 4px solid var(--ink); margin-left: 3px; vertical-align: 1px; }
  .account-link { position: absolute; left: 872px; top: 0; width: 166px; height: 26px; border-left: 1px solid var(--teal); border-right: 1px solid var(--teal); color: var(--teal); font-size: 10px; display: flex; align-items: center; justify-content: center; gap: 5px; }

  .main-nav { position: absolute; top: 26px; left: 0; width: 1200px; height: 64px; background: var(--nav-bg); }
  .brand { position: absolute; left: 162px; top: 10px; display: flex; align-items: center; gap: 9px; }
  .brand-dot { width: 44px; height: 44px; border-radius: 50%; background: var(--teal); }
  .brand-name { color: var(--white); font-size: 20px; font-weight: 500; }
  .nav-links { position: absolute; top: 24px; left: 0; font-size: 11px; color: var(--white); }
  .nav-links a { position: absolute; white-space: nowrap; color: var(--white); text-decoration: none; line-height: 18px; }
  .nav-links a.active { background: var(--teal); border-radius: 9px; padding: 0 10px; width: 68px; text-align: center; }
  .partner-btn { position: absolute; left: 912px; top: 21px; width: 126px; height: 22px; border-radius: 11px; background: var(--white); color: var(--teal); font-size: 10.5px; display: flex; align-items: center; justify-content: center; gap: 4px; }

  .hero-backdrop { position: absolute; top: 90px; left: 0; width: 1200px; height: 451px;
    background: linear-gradient(180deg, #ffffff 0%, #ffffff 22%, #e6ebe8 32%, #a8b4aa 45%, #6f7f6c 58%, #5e6757 72%, #55594c 86%, #4b4a40 100%); }

  .hero-title { position: absolute; top: 146px; left: 0; width: 1200px; text-align: center; font-size: 29px; font-weight: 700; letter-spacing: 0.2px; color: var(--ink); }
  .hero-subtitle { position: absolute; top: 183px; left: 0; width: 1200px; text-align: center; font-size: 17px; color: var(--teal); }

  .search-card { position: absolute; left: 311px; top: 226px; width: 577px; height: 253px; background: var(--white); }
  .search-tabs { display: flex; height: 37px; border-bottom: 1px solid #c9ccd0; }
  .search-tabs .tab { flex: 1; display: flex; align-items: center; justify-content: center; font-size: 14px; font-weight: 500; color: var(--ink); border-left: 1px solid #e2e2e2; }
  .search-tabs .tab:first-child { border-left: 0; }
  .search-tabs .tab.active { background: var(--teal); color: var(--white); }
  .field { position: absolute; height: 37px; border: 1px solid var(--field-border); font-family: "Open Sans", sans-serif; font-weight: 300; font-size: 11.5px; color: #666; display: flex; align-items: center; padding-left: 10px; }
  .field.dates { padding: 0; }
  .field.dates span { flex: 1; padding-left: 11px; }
  .field.dates span + span { border-left: 1px solid var(--field-border); height: 25px; display: flex; align-items: center; }
  .search-btn { position: absolute; left: 241px; top: 170px; width: 97px; height: 37px; border-radius: 19px; background: var(--teal); color: var(--white); font-family: "Open Sans", sans-serif; font-size: 11.5px; display: flex; align-items: center; justify-content: center; }
  .search-stats { position: absolute; top: 224px; left: 151px; font-family: "Open Sans", sans-serif; font-weight: 300; font-size: 10px; color: #666; display: flex; align-items: center; white-space: nowrap; }
  .search-stats svg { margin-right: 2px; }
  .search-stats .count + .count { margin-left: 8px; }
  .search-stats .advanced { margin-left: 18px; color: var(--teal); font-family: "Ubuntu", sans-serif; font-weight: 500; }
</style>
</head>
<body>

<header class="utility-bar">
  <div class="lang">Magyar<span class="caret"></span></div>
  <div class="currency">EUR<span class="caret"></span></div>
  <div class="account-link">
    <svg width="8" height="9" viewBox="0 0 8 9"><circle cx="4" cy="2.3" r="2.1" fill="#65ae97"/><path d="M0 9c0-3 1.8-4.3 4-4.3S8 6 8 9z" fill="#65ae97"/></svg>
    Regisztráció / Bejelentkezés
  </div>
</header>

<nav class="main-nav">
  <div class="brand">
    <span class="brand-dot"></span>
    <span class="brand-name">ferntrail.online</span>
  </div>
  <div class="nav-links">
    <a class="active" style="left:540px">Országok</a>
    <a style="left:617px">Vadfajok</a>
    <a style="left:686px">Rólunk</a>
    <a style="left:746px">ÁSZF</a>
    <a style="left:795px">Hogyan működik</a>
  </div>
  <div class="partner-btn">
    <svg width="10" height="10" viewBox="0 0 10 10"><circle cx="5" cy="5" r="5" fill="#65ae97"/><path d="M5 2.4v5.2M2.4 5h5.2" stroke="#fff" stroke-width="1.4"/></svg>
    Legyen partnerünk
  </div>
</nav>

<div class="hero-backdrop" role="img" aria-label="Változó természetfotó: ködös fenyőerdő egy sziklás, moszatos tengerparti öböl mentén"></div>

<h1 class="hero-title">NINCS SZÜKSÉGED VADÁSZATSZERVEZŐRE!</h1>
<p class="hero-subtitle">Foglalj közvetlen a vadászterületnél</p>

<section class="search-card">
  <div class="search-tabs">
    <div class="tab active">Egyéni vadászatok</div>
    <div class="tab">Egyéni vadászatok</div>
    <div class="tab">Egyéni vadászatok</div>
  </div>
  <div class="field" style="left:30px;top:69px;width:251px">Összes vad</div>
  <div class="field" style="left:296px;top:69px;width:251px">Összes ország</div>
  <div class="field" style="left:30px;top:118px;width:251px">Összes ajánlat</div>
  <div class="field dates" style="left:296px;top:118px;width:251px"><span>Augusztus 2019</span><span>Augusztus 2019</span></div>
  <div class="search-btn">KERESÉS</div>
  <div class="search-stats">
    <span class="count"><svg width="7" height="10" viewBox="0 0 7 10"><path d="M3.5 0A3.5 3.5 0 0 0 0 3.5C0 6 3.5 10 3.5 10S7 6 7 3.5A3.5 3.5 0 0 0 3.5 0z" fill="#777"/><circle cx="3.5" cy="3.5" r="1.3" fill="#fff"/></svg>123456 terület</span>
    <span class="count"><svg width="10" height="10" viewBox="0 0 10 10" fill="none" stroke="#777" stroke-width="1"><circle cx="5" cy="5" r="3.6"/><path d="M5 0v3M5 7v3M0 5h3M7 5h3"/></svg>87654321 ajánlat</span>
    <span class="advanced">Részletes keresés</span>
  </div>
</section>

</body>
</html>
```